Clerical Business Card Design

I have just started a new business focusing on Clerical / Administration Support for Small to Medium sized Businesses. I can provide support not just only my local area but anywhere as long as it is able to be done over the internet/email. I am the only person working in the business.
I would like to see some designs that are bright in colour yet a clean fresh design. The design should communicate balance.
Updates

Target Market(s)

Small to Medium sized Professional Businesses

Industry/Entity Type

Business

Contact Information for Business Card

Business Name: Vormley's Clerical
Statement: Providing Balanced Efficient Support
My Name: Ilsa Vormley
Phone: 0418 571 924 or 02 6519 4027
Email: vormleysclerical@plimmet.com.au

Colors

Designer to choose colors to be used in the design.

Requirements
Must have
• I'm open to suggestions
Nice to have
• I would like to see maybe something done with the two "C" in the business name whether that could be a focus of difference
Should not have
• Cartoon type pictures

```html
<!DOCTYPE html>
<html lang="en">
<head>
<meta charset="utf-8">
<title>Vormley's Clerical – Business Card</title>
<link rel="stylesheet" href="https://fonts.googleapis.com/css2?family=Sorts+Mill+Goudy&display=swap">
<style>
  :root {
    --card-green: #acd136;
    --ink: #2e2e2a;
    --band-white: #ffffff;
    --icon-green: #a9cf36;
  }
  * { margin: 0; padding: 0; box-sizing: border-box; }
  html, body {
    width: 1200px;
    height: 725px;
    overflow: hidden;
    background: var(--card-green);
  }
  .card {
    position: relative;
    width: 1200px;
    height: 725px;
    overflow: hidden;
    background: var(--card-green);
    color: var(--ink);
    font-family: "Sorts Mill Goudy", Georgia, serif;
  }
  .brand-name {
    position: absolute;
    left: 104px;
    top: 88px;
    font-size: 88px;
    line-height: 1.15;
    font-weight: 400;
    letter-spacing: 1px;
    color: var(--ink);
  }
  .tagline {
    position: absolute;
    left: 660px;
    top: 138px;
    width: 432px;
    text-align: center;
    font-size: 42px;
    line-height: 1.22;
  }
  .holder-name {
    position: absolute;
    left: 0;
    width: 1248px;
    top: 405px;
    text-align: center;
    font-size: 50px;
  }
  .contact-band {
    position: absolute;
    left: 0;
    top: 602px;
    width: 1200px;
    height: 73px;
    background: var(--band-white);
  }
  .contact-icon { position: absolute; }
  .icon-phone { left: 68px; top: 10px; }
  .icon-mail { left: 614px; top: 11px; }
  .contact-text {
    position: absolute;
    top: 50%;
    transform: translateY(-50%);
    white-space: nowrap;
  }
  .phone-numbers { left: 142px; font-size: 38px; }
  .email-address { left: 716px; font-size: 30px; }
</style>
</head>
<body>
  <main class="card">
    <h1 class="brand-name">Vormley's<br>Clerical</h1>

    <p class="tagline">Providing Balanced<br>Efficient Support</p>

    <p class="holder-name">Ilsa Vormley</p>

    <footer class="contact-band">
      <svg class="contact-icon icon-phone" width="44" height="53" viewBox="0 0 44 53" aria-hidden="true">
        <ellipse cx="22" cy="26.5" rx="19.5" ry="24" fill="none" stroke="var(--icon-green)" stroke-width="3"/>
        <path d="M27 12 c-4 1 -8 4 -9.5 10 c-1.5 6 -1 12 2 17 l3 -2 c-2.5 -4 -3 -9 -2 -13.5 c1 -4.5 3.5 -7 7.5 -8.5 z" fill="var(--icon-green)"/>
        <rect x="24" y="9" width="7" height="6" rx="2" fill="var(--icon-green)"/>
        <rect x="18" y="36" width="7" height="6" rx="2" fill="var(--icon-green)"/>
      </svg>
      <span class="contact-text phone-numbers">0418 571 924 / 02 6519 4027</span>

      <svg class="contact-icon icon-mail" width="74" height="52" viewBox="0 0 74 52" aria-hidden="true">
        <rect x="3" y="3" width="68" height="46" fill="none" stroke="var(--icon-green)" stroke-width="5"/>
        <path d="M5 5 L37 30 L69 5" fill="none" stroke="var(--icon-green)" stroke-width="5"/>
        <path d="M5 47 L28 24 M69 47 L46 24" fill="none" stroke="var(--icon-green)" stroke-width="5"/>
      </svg>
      <span class="contact-text email-address">vormleysclerical@plimmet.com.au</span>
    </footer>
  </main>
</body>
</html>
```